Brightwater Systems Website

I am starting an IT consulting business called Brightwater Systems. I recently completed a logo contest on ArtHive and am now looking to put together a basic website. I can provide text and content but am looking for a site design with layout and graphics. I am attaching my logo below. I was thinking of a dark blue and white theme for the website (similar to the logo). However, I am open to ideas. Graphics can be a mix of business and high tech as that is the image I am trying to convey. The site will be relatively simple and probably have only 3 - 5 pages (Home, About Us, Services, Contact, etc.)
Target Market(s)
United States commercial companies and government contractors
Industry/Entity Type
Consulting
Coding
Coded - Design and coding required
Number of Pages Required
4 page
Look and feel

```html
<!DOCTYPE html>
<html lang="en">
<head>
<meta charset="utf-8">
<title>Brightwater Systems – IT Consulting</title>
<link href="https://fonts.googleapis.com/css2?family=Poppins:wght@400;500;600;700&display=swap" rel="stylesheet">
<style>
:root{
  --navy:#27306e;
  --navy-deep:#1f2860;
  --title:#283474;
  --blue:#0d9ad9;
  --blue-soft:#3fb2e8;
  --text:#3b4274;
  --muted:#6a7096;
  --white:#ffffff;
  --line:#c9d3e6;
}
*{box-sizing:border-box;margin:0;padding:0}
html,body{width:1200px;height:4804px;overflow:hidden;background:var(--white)}
body{font-family:'Poppins',sans-serif;color:var(--text);position:relative}
.page{position:relative;width:1200px;height:4804px;overflow:hidden}
.abs{position:absolute}
.btn{position:absolute;display:flex;align-items:center;justify-content:center;border-radius:20px;font-size:10.5px;font-weight:600;letter-spacing:.3px;color:var(--white);background:var(--blue);text-transform:uppercase}
.btn.ghost{background:transparent;border:1.5px solid var(--white)}
.section-title{position:absolute;left:0;width:1200px;text-align:center;font-size:22px;font-weight:600;color:var(--title);letter-spacing:.2px}
.intro{position:absolute;left:160px;width:880px;text-align:center;font-size:11px;line-height:17px;color:var(--muted)}
.on-dark{color:var(--white)}
.brand{font-weight:500;color:var(--white);letter-spacing:3px;display:flex;align-items:center;gap:10px}
.brand .dot{width:14px;height:14px;border-radius:50%;background:var(--blue)}

/* hero */
.hero-bg{left:0;top:0;width:1200px;height:606px;background:linear-gradient(120deg,#3a4fa0 0%,#5068b4 40%,#6d85c7 70%,#4c63ad 100%)}
.hero-shade{left:0;top:0;width:1200px;height:606px;background:linear-gradient(90deg,rgba(30,40,110,.55),rgba(30,40,110,.1))}
.nav a{position:absolute;font-size:11px;font-weight:500;color:var(--white);text-decoration:none;white-space:nowrap}
.hero-title{left:157px;top:226px;font-size:22px;font-weight:600;color:var(--white)}
.hero-text{left:157px;top:263px;width:420px;font-size:10.8px;line-height:15.2px;font-weight:500;color:var(--white);text-align:justify}
.divider{position:absolute;left:0;width:1200px}
.emblem{position:absolute;width:60px;height:60px;border-radius:50%;background:var(--white);border:5px solid var(--blue);box-shadow:0 0 0 5px var(--white)}

/* services */
.map-fade{left:40px;top:620px;width:1120px;height:520px;background:radial-gradient(ellipse at 40% 30%,rgba(150,175,215,.18),rgba(255,255,255,0) 65%)}
.photo{position:absolute;top:769px;width:274px;height:280px}
.svc-title{position:absolute;top:1075px;width:274px;font-size:12px;font-weight:600;color:var(--title)}
.svc-text{position:absolute;top:1110px;width:274px;font-size:9.6px;line-height:16.5px;color:var(--muted);text-align:justify}
.lead{left:200px;top:1278px;width:800px;text-align:center;font-size:12.4px;font-weight:600;line-height:20px;color:var(--title)}

/* process */
.process-bg{left:0;top:1454px;width:1200px;height:627px;background:var(--navy)}
.globe{left:820px;top:1460px;width:380px;height:380px;background:radial-gradient(circle at 70% 40%,rgba(120,145,210,.28),rgba(39,48,110,0) 65%)}
.step-ring{position:absolute;top:1655px;width:116px;height:116px}
.step-title{position:absolute;top:1783px;width:188px;text-align:center;font-size:14px;font-weight:600;color:var(--white)}
.step-text{position:absolute;top:1820px;width:188px;font-size:11px;line-height:17.6px;color:var(--white);text-align:justify}

/* tech */
.tech-icon{position:absolute;width:80px;height:80px}
.tech-title{position:absolute;width:260px;text-align:center;font-size:11.5px;font-weight:500;color:var(--title)}
.tech-text{position:absolute;width:230px;text-align:center;font-size:10.6px;line-height:17px;color:var(--muted)}

/* get started */
.start-bg{left:0;top:2790px;width:1200px;height:295px;background:var(--navy)}
.start-photo{left:578px;top:2790px;width:622px;height:295px;background:linear-gradient(110deg,#27306e 0%,#2e4a98 30%,#3a78c4 55%,#2c3f8a 80%,#1e2a66 100%)}
.start-title{left:157px;top:2883px;font-size:20px;font-weight:500;color:var(--white)}
.start-text{left:157px;top:2914px;width:380px;font-size:11px;line-height:17px;color:var(--white)}

/* testimonials */
.card{position:absolute;top:3247px;width:286px;height:283px;background:var(--white);border-radius:18px;box-shadow:0 6px 22px rgba(40,52,116,.18)}
.card .q{position:absolute;font-size:64px;font-weight:700;color:#d7dbe6;line-height:1}
.card .q.open{left:24px;top:10px}
.card .q.close{right:24px;top:168px}
.card p{position:absolute;left:24px;top:58px;width:240px;font-size:8.6px;line-height:14px;color:var(--muted)}
.card h4{position:absolute;left:0;top:225px;width:100%;text-align:center;font-size:10.5px;font-weight:600;color:var(--title)}
.dots{left:574px;top:3595px;display:flex;gap:8px}
.dots span{width:11px;height:11px;border-radius:50%;border:1.5px solid var(--blue)}

/* contact */
.contact-bg{left:0;top:3708px;width:1200px;height:680px;background:linear-gradient(100deg,#2e3c80 0%,#4f63a8 35%,#6a7fbf 60%,#3d4f96 100%)}
.form-card{left:383px;top:3764px;width:432px;height:472px;background:var(--white);border-radius:20px}
.form-title{left:422px;top:3800px;font-size:19px;font-weight:600;color:var(--title)}
.form-sub{left:422px;top:3836px;width:360px;font-size:10px;line-height:16px;color:var(--muted)}
.field{position:absolute;height:30px;border:1.3px solid var(--blue-soft);border-radius:16px;font-size:8.5px;color:var(--muted);padding:0 12px;display:flex;align-items:center;justify-content:space-between}
.field.area{align-items:flex-start;padding-top:12px;border-radius:18px}
.form-note{left:422px;top:4166px;width:356px;font-size:7.4px;line-height:11px;color:var(--muted)}

/* footer */
.footer-bg{left:0;top:4361px;width:1200px;height:443px;background:var(--navy)}
.foot-col{position:absolute;top:4494px}
.foot-col h5{font-size:11.5px;font-weight:600;color:var(--white);padding-bottom:6px;border-bottom:1px solid rgba(255,255,255,.25);width:120px;margin-bottom:8px}
.foot-col li{list-style:none;font-size:9.6px;line-height:22.4px;color:var(--white);white-space:nowrap}
.foot-col .ci{display:flex;align-items:center;gap:8px}
.copy{left:0;top:4777px;width:1200px;height:27px;background:var(--blue);color:var(--white);font-size:9.5px;display:flex;align-items:center;justify-content:center}
</style>
</head>
<body>
<div class="page">

  <!-- HERO -->
  <div class="abs hero-bg" role="img" aria-label="Photo of a business desk with printed charts and coffee cups, tinted blue"></div>
  <div class="abs hero-shade"></div>

  <div class="abs brand" style="left:157px;top:40px;font-size:22px">
    <span class="dot"></span>BRIGHTWATER SYSTEMS
  </div>

  <nav class="abs nav" style="left:0;top:50px;width:1200px;height:20px">
    <a style="left:649px">HOME</a>
    <a style="left:712px">ABOUT US</a>
    <a style="left:797px">SERVICES</a>
    <a style="left:881px">FAQ</a>
  </nav>
  <div class="btn" style="left:933px;top:46px;width:108px;height:24px;font-size:9px">Get in touch</div>

  <h1 class="abs hero-title">IT CONSULTING SERVICES</h1>
  <p class="abs hero-text">Lorem ipsum dolor sit amet, consectetur adipiscing elit, sed do eiusmod tempor incididunt ut labore et dolore magna aliqua. Quis ipsum suspendisse ultrices gravida. Risus commodo viverra maecenas accumsan lacus vel facilisis. Lorem ipsum dolor sit amet, consectetur adipiscing elit, sed do eiusmod tempor incididunt ut labore et dolore magna aliqua. Quis ipsum suspendisse ultrices gravida.dolore magna aliqua. Quis ipsum suspendisse ultrices</p>
  <div class="btn" style="left:159px;top:390px;width:149px;height:34px">Our services</div>
  <div class="btn ghost" style="left:319px;top:390px;width:149px;height:34px">Get in touch</div>

  <svg class="divider" style="top:520px" width="1200" height="90" viewBox="0 0 1200 90" aria-hidden="true">
    <path d="M0 86 C260 40 460 40 600 40 C740 40 940 40 1200 86 L1200 90 L0 90 Z" fill="#ffffff"/>
    <path d="M70 78 C260 44 460 36 600 36 C740 36 940 44 1130 78" fill="none" stroke="#0d9ad9" stroke-width="4"/>
  </svg>
  <div class="emblem" style="left:570px;top:537px"></div>

  <!-- SERVICES -->
  <div class="abs map-fade" role="img" aria-label="Faint dotted world map"></div>
  <h2 class="section-title" style="top:638px">OUR IT CONSULTING SERVICES</h2>
  <p class="intro" style="top:678px">Lorem ipsum dolor sit amet, consectetur adipiscing elit, sed do eiusmod tempor incididunt ut labore et dolore magna aliqua. Quis ipsum suspendisse ultrices gravida. Risus commodo viverra maecenas accumsan lacus vel facilisis. Lorem ipsum dolor sit amet, consectetur adipiscing elit, sed do eiusmod tempor incididunt ut labore et dolore magna aliqua.</p>

  <div class="photo" style="left:159px;background:linear-gradient(150deg,#7a5a44,#a8866a 50%,#3b3d44)" role="img" aria-label="Photo of hands working on a laptop on a wooden desk"></div>
  <div class="photo" style="left:463px;background:linear-gradient(150deg,#cfd3d8,#8f96a0 50%,#e2e4e7)" role="img" aria-label="Photo of a team meeting around a table with tablets and papers"></div>
  <div class="photo" style="left:767px;background:linear-gradient(150deg,#e9e4e2,#c9b7b0 50%,#6f6c72)" role="img" aria-label="Photo of a person typing on a laptop showing a website"></div>

  <h3 class="svc-title" style="left:159px">ENTERPRISE ARCHITECTURE ADVISORY</h3>
  <h3 class="svc-title" style="left:463px">IT STRATEGY CONSULTING &amp; NEW TECH</h3>
  <h3 class="svc-title" style="left:767px">SOFTWARE PORTFOLIO CONSULTING</h3>
  <p class="svc-text" style="left:159px">Lorem ipsum dolor sit amet, consectetur adipiscing elit, sed do eiusmod tempor incididunt ut labore et dolore magna aliqua. Quis ipsum suspendisse ultrices gravida. Risus commodo viverra maecenas accumsan lacus vel facilisis. Lorem ipsum dolor sit amet, consectetur adipiscing elit, sed do eiusmod tempor incididunt ut labore et dolore magna aliqua.</p>
  <p class="svc-text" style="left:463px">Lorem ipsum dolor sit amet, consectetur adipiscing elit, sed do eiusmod tempor incididunt ut labore et dolore magna aliqua. Quis ipsum suspendisse ultrices gravida. Risus commodo viverra maecenas accumsan lacus vel facilisis. Lorem ipsum dolor sit amet, consectetur adipiscing elit, sed do eiusmod tempor incididunt ut labore et dolore magna aliqua.</p>
  <p class="svc-text" style="left:767px">Lorem ipsum dolor sit amet, consectetur adipiscing elit, sed do eiusmod tempor incididunt ut labore et dolore magna aliqua. Quis ipsum suspendisse ultrices gravida. Risus commodo viverra maecenas accumsan lacus vel facilisis. Lorem ipsum dolor sit amet, consectetur adipiscing elit, sed do eiusmod tempor incididunt ut labore et dolore magna aliqua.</p>

  <p class="abs lead">Lorem ipsum dolor sit amet, consectetur adipiscing elit, sed do eiusmod tempor incididunt ut labore et dolore magna aliqua. Quis ipsum suspendisse ultrices gravida. Risus commodo viverra maecenas accumsan lacus vel facilisis.</p>
  <div class="btn" style="left:524px;top:1348px;width:150px;height:34px">Contact us</div>

  <!-- PROCESS -->
  <div class="abs process-bg"></div>
  <div class="abs globe" role="img" aria-label="Faint globe graphic"></div>
  <div class="emblem" style="left:570px;top:1424px"></div>
  <h2 class="section-title on-dark" style="top:1515px">OUR IT CONSULTING PROCESS</h2>
  <p class="intro on-dark" style="top:1555px">Lorem ipsum dolor sit amet, consectetur adipiscing elit, sed do eiusmod tempor incididunt ut labore et dolore magna aliqua. Quis ipsum suspendisse ultrices gravida. Risus commodo viverra maecenas accumsan lacus vel facilisis. Lorem ipsum dolor sit amet, consectetur adipiscing elit, sed do eiusmod tempor incididunt ut labore et dolore magna aliqua.</p>

  <svg class="step-ring" style="left:194px" viewBox="0 0 116 116" aria-hidden="true">
    <circle cx="58" cy="58" r="50" fill="none" stroke="#0d9ad9" stroke-width="9" stroke-dasharray="250 64" transform="rotate(-60 58 58)"/>
    <circle cx="58" cy="58" r="34" fill="none" stroke="#ffffff" stroke-width="1.5"/>
    <circle cx="54" cy="54" r="14" fill="none" stroke="#3fb2e8" stroke-width="3"/>
    <path d="M64 64 L78 78" stroke="#3fb2e8" stroke-width="4" stroke-linecap="round"/>
  </svg>
  <svg class="step-ring" style="left:427px" viewBox="0 0 116 116" aria-hidden="true">
    <circle cx="58" cy="58" r="50" fill="none" stroke="#0d9ad9" stroke-width="9" stroke-dasharray="250 64" transform="rotate(-60 58 58)"/>
    <circle cx="58" cy="58" r="34" fill="none" stroke="#ffffff" stroke-width="1.5"/>
    <path d="M44 74 L58 40 L72 74 Z" fill="none" stroke="#3fb2e8" stroke-width="3"/>
    <circle cx="58" cy="58" r="5" fill="#3fb2e8"/>
  </svg>
  <svg class="step-ring" style="left:660px" viewBox="0 0 116 116" aria-hidden="true">
    <circle cx="58" cy="58" r="50" fill="none" stroke="#0d9ad9" stroke-width="9" stroke-dasharray="250 64" transform="rotate(-60 58 58)"/>
    <circle cx="58" cy="58" r="34" fill="none" stroke="#ffffff" stroke-width="1.5"/>
    <circle cx="58" cy="58" r="18" fill="none" stroke="#3fb2e8" stroke-width="6" stroke-dasharray="6 4"/>
    <circle cx="58" cy="58" r="7" fill="none" stroke="#3fb2e8" stroke-width="3"/>
  </svg>
  <svg class="step-ring" style="left:890px" viewBox="0 0 116 116" aria-hidden="true">
    <circle cx="58" cy="58" r="50" fill="none" stroke="#0d9ad9" stroke-width="9" stroke-dasharray="250 64" transform="rotate(-60 58 58)"/>
    <circle cx="58" cy="58" r="34" fill="none" stroke="#ffffff" stroke-width="1.5"/>
    <rect x="42" y="60" width="8" height="16" fill="#3fb2e8"/>
    <rect x="54" y="50" width="8" height="26" fill="#3fb2e8"/>
    <rect x="66" y="42" width="8" height="34" fill="#3fb2e8"/>
  </svg>

  <h3 class="step-title" style="left:159px">ANALYSIS</h3>
  <h3 class="step-title" style="left:392px">STRATEGY</h3>
  <h3 class="step-title" style="left:625px">PERFORMANCE</h3>
  <h3 class="step-title" style="left:855px">IMPROVEMENTS</h3>
  <p class="step-text" style="left:159px">Lorem ipsum dolor sit amet, consectetur adipiscing elit, sed do eiusmod tempor incididunt ut labore et dolore magna aliqua. Quis ipsum suspendisse ultrices gravida. Risus commodo viverra maecenas accumsan lacus vel facilisis. Lorem ipsum dolor sit amet, consectetur adipiscing elit, sed do eiusmod</p>
  <p class="step-text" style="left:392px">Lorem ipsum dolor sit amet, consectetur adipiscing elit, sed do eiusmod tempor incididunt ut labore et dolore magna aliqua. Quis ipsum suspendisse ultrices gravida. Risus commodo viverra maecenas accumsan lacus vel facilisis. Lorem ipsum dolor sit amet, consectetur adipiscing elit, sed do eiusmod</p>
  <p class="step-text" style="left:625px">Lorem ipsum dolor sit amet, consectetur adipiscing elit, sed do eiusmod tempor incididunt ut labore et dolore magna aliqua. Quis ipsum suspendisse ultrices gravida. Risus commodo viverra maecenas accumsan lacus vel facilisis. Lorem ipsum dolor sit amet, consectetur adipiscing elit, sed do eiusmod</p>
  <p class="step-text" style="left:855px">Lorem ipsum dolor sit amet, consectetur adipiscing elit, sed do eiusmod tempor incididunt ut labore et dolore magna aliqua. Quis ipsum suspendisse ultrices gravida. Risus commodo viverra maecenas accumsan lacus vel facilisis. Lorem ipsum dolor sit amet, consectetur adipiscing elit, sed do eiusmod</p>

  <!-- TECHNOLOGIES -->
  <div class="abs map-fade" style="top:2240px;height:520px" role="img" aria-label="Faint dotted world map"></div>
  <h2 class="section-title" style="top:2163px">LOREM IPSUM DOLOR SIT AMET</h2>
  <p class="intro" style="top:2204px">Lorem ipsum dolor sit amet, consectetur adipiscing elit, sed do eiusmod tempor incididunt ut labore et dolore magna aliqua. Quis ipsum suspendisse ultrices gravida. Risus commodo viverra maecenas accumsan lacus vel facilisis. Lorem ipsum dolor sit amet, consectetur adipiscing elit, sed do eiusmod tempor incididunt ut labore et dolore magna aliqua.</p>

  <svg class="tech-icon" style="left:231px;top:2300px" viewBox="0 0 80 80" aria-hidden="true" fill="none" stroke="#0d9ad9" stroke-width="2.5">
    <path d="M40 6 L70 23 L70 57 L40 74 L10 57 L10 23 Z"/>
    <path d="M40 22 L56 31 L56 49 L40 58 L24 49 L24 31 Z M24 31 L40 40 L56 31 M40 40 L40 58"/>
  </svg>
  <svg class="tech-icon" style="left:548px;top:2300px" viewBox="0 0 80 80" aria-hidden="true" fill="none" stroke="#0d9ad9" stroke-width="2.5">
    <rect x="18" y="14" width="44" height="20" rx="8"/>
    <path d="M22 74 C22 58 30 50 40 50 C50 50 58 58 58 74"/>
    <path d="M40 34 L40 50"/>
  </svg>
  <svg class="tech-icon" style="left:867px;top:2300px" viewBox="0 0 80 80" aria-hidden="true" fill="none" stroke="#0d9ad9" stroke-width="2.5">
    <rect x="22" y="18" width="36" height="44" rx="6"/>
    <path d="M12 28 H22 M12 40 H22 M12 52 H22 M58 28 H68 M58 40 H68 M58 52 H68"/>
    <circle cx="40" cy="40" r="8"/>
  </svg>

  <h3 class="tech-title" style="left:141px;top:2385px">BLOCKCHAIN TECHNOLOGY</h3>
  <h3 class="tech-title" style="left:458px;top:2385px">AUGMENTED REALITY</h3>
  <h3 class="tech-title" style="left:777px;top:2385px">ARTIFICIAL INTELLIGENCE</h3>
  <p class="tech-text" style="left:156px;top:2413px">Lorem ipsum dolor sit amet, consectetur adipiscing elit, sed do eiusmod tempor incididunt ut labore et dolore magna aliqua.</p>
  <p class="tech-text" style="left:473px;top:2413px">Lorem ipsum dolor sit amet, consectetur adipiscing elit, sed do eiusmod tempor incididunt ut labore et dolore magna aliqua.</p>
  <p class="tech-text" style="left:792px;top:2413px">Lorem ipsum dolor sit amet, consectetur adipiscing elit, sed do eiusmod tempor incididunt ut labore et dolore magna aliqua.</p>

  <svg class="tech-icon" style="left:231px;top:2532px" viewBox="0 0 80 80" aria-hidden="true" fill="none" stroke="#0d9ad9" stroke-width="2.5">
    <path d="M24 30 C14 30 14 16 26 16 C28 6 48 6 50 16 C64 14 66 30 56 30 Z"/>
    <path d="M40 30 V44 M24 44 H56 M24 44 V52 M56 44 V52"/>
    <rect x="14" y="52" width="20" height="24" rx="3"/>
    <rect x="46" y="52" width="20" height="24" rx="3"/>
  </svg>
  <svg class="tech-icon" style="left:548px;top:2532px" viewBox="0 0 80 80" aria-hidden="true" fill="none" stroke="#0d9ad9" stroke-width="2.5">
    <path d="M20 46 C6 46 6 26 22 26 C24 10 52 8 56 24 C74 22 76 46 60 46 Z"/>
    <path d="M28 46 V60 M40 46 V68 M52 46 V60"/>
    <circle cx="28" cy="63" r="3"/><circle cx="40" cy="71" r="3"/><circle cx="52" cy="63" r="3"/>
  </svg>
  <svg class="tech-icon" style="left:867px;top:2532px" viewBox="0 0 80 80" aria-hidden="true" fill="none" stroke="#0d9ad9" stroke-width="2.5">
    <circle cx="28" cy="24" r="11"/><circle cx="54" cy="24" r="11"/>
    <path d="M28 18 V30 M54 18 V30"/>
    <rect x="14" y="48" width="22" height="22"/><rect x="44" y="48" width="22" height="22"/>
  </svg>

  <h3 class="tech-title" style="left:141px;top:2630px">INTERNET OF THINGS</h3>
  <h3 class="tech-title" style="left:458px;top:2630px">CLOUD COMPUTING</h3>
  <h3 class="tech-title" style="left:777px;top:2630px">FINTECH</h3>
  <p class="tech-text" style="left:156px;top:2652px">Lorem ipsum dolor sit amet, consectetur adipiscing elit, sed do eiusmod tempor incididunt ut labore et dolore magna aliqua.</p>
  <p class="tech-text" style="left:473px;top:2652px">Lorem ipsum dolor sit amet, consectetur adipiscing elit, sed do eiusmod tempor incididunt ut labore et dolore magna aliqua.</p>
  <p class="tech-text" style="left:792px;top:2652px">Lorem ipsum dolor sit amet, consectetur adipiscing elit, sed do eiusmod tempor incididunt ut labore et dolore magna aliqua.</p>

  <!-- GET STARTED -->
  <div class="abs start-bg"></div>
  <div class="abs start-photo" role="img" aria-label="Photo of a hand touching glowing hexagons with words such as consulting, knowledge, service, support, experience, success and expert"></div>
  <h2 class="abs start-title">GET STARTED</h2>
  <p class="abs start-text">Lorem ipsum dolor sit amet, consectetur adipiscing elit, sed do eiusmod tempor incididunt ut labore et dolore magna aliqua.</p>
  <div class="btn" style="left:159px;top:2961px;width:127px;height:28px;font-size:11px">Talk to us</div>

  <!-- TESTIMONIALS -->
  <h2 class="section-title" style="top:3160px">WHAT OUR CLIENTS SAY</h2>
  <div class="card" style="left:131px">
    <span class="q open">“</span><span class="q close">”</span>
    <p>Lorem ipsum dolor sit amet, consectetur adipiscing elit, sed do eiusmod tempor incididunt ut labore et dolore magna aliqua. Quis ipsum suspendisse ultrices gravida. Risus commodo viverra maecenas accumsan lacus vel facilisis. Lorem ipsum dolor sit amet, consectetur adipiscing elit, sed do eiusmod tempor incididunt ut labore et dolore magna aliqua. Quis ipsum suspendisse ultrices gravida. Risus commodo viverra maecenas accumsan lacus vel facilisis.</p>
    <h4>COMPANY NAME</h4>
  </div>
  <div class="card" style="left:461px">
    <span class="q open">“</span><span class="q close">”</span>
    <p>Lorem ipsum dolor sit amet, consectetur adipiscing elit, sed do eiusmod tempor incididunt ut labore et dolore magna aliqua. Quis ipsum suspendisse ultrices gravida. Risus commodo viverra maecenas accumsan lacus vel facilisis. Lorem ipsum dolor sit amet, consectetur adipiscing elit, sed do eiusmod tempor incididunt ut labore et dolore magna aliqua. Quis ipsum suspendisse ultrices gravida. Risus commodo viverra maecenas accumsan lacus vel facilisis.</p>
    <h4>COMPANY NAME</h4>
  </div>
  <div class="card" style="left:780px">
    <span class="q open">“</span><span class="q close">”</span>
    <p>Lorem ipsum dolor sit amet, consectetur adipiscing elit, sed do eiusmod tempor incididunt ut labore et dolore magna aliqua. Quis ipsum suspendisse ultrices gravida. Risus commodo viverra maecenas accumsan lacus vel facilisis. Lorem ipsum dolor sit amet, consectetur adipiscing elit, sed do eiusmod tempor incididunt ut labore et dolore magna aliqua. Quis ipsum suspendisse ultrices gravida. Risus commodo viverra maecenas accumsan lacus vel facilisis.</p>
    <h4>COMPANY NAME</h4>
  </div>
  <div class="abs dots"><span></span><span></span><span></span></div>

  <!-- CONTACT -->
  <div class="abs contact-bg" role="img" aria-label="Photo of office workers at desks, tinted blue"></div>
  <div class="abs form-card"></div>
  <h2 class="abs form-title">GET IN TOUCH WITH US</h2>
  <p class="abs form-sub">Please provide contact information below to schedule an appointment or request additional information.</p>
  <div class="field" style="left:422px;top:3898px;width:171px">First Name</div>
  <div class="field" style="left:605px;top:3898px;width:173px">Last Name</div>
  <div class="field" style="left:422px;top:3944px;width:171px">Email Address</div>
  <div class="field" style="left:605px;top:3944px;width:173px">Contact Number</div>
  <div class="field" style="left:422px;top:3991px;width:171px">Service
    <svg width="8" height="6" viewBox="0 0 8 6" aria-hidden="true"><path d="M1 1 L4 4 L7 1" fill="none" stroke="#3b4274" stroke-width="1.3"/></svg></div>
  <div class="field" style="left:605px;top:3991px;width:173px">Country
    <svg width="8" height="6" viewBox="0 0 8 6" aria-hidden="true"><path d="M1 1 L4 4 L7 1" fill="none" stroke="#3b4274" stroke-width="1.3"/></svg></div>
  <div class="field area" style="left:422px;top:4038px;width:356px;height:69px">Message</div>
  <div class="btn" style="left:683px;top:4128px;width:95px;height:24px;font-size:10.5px">Submit</div>
  <p class="abs form-note">Lorem ipsum dolor sit amet, consectetur adipiscing elit, sed do eiusmod tempor incididunt ut labore et dolore magna aliqua. Quis ipsum suspendisse ultrices gravida. Risus commodo viverra maecenas accumsan lacus vel facilisis. Lorem ipsum dolor sit amet.</p>

  <!-- FOOTER -->
  <div class="abs footer-bg"></div>
  <svg class="divider" style="top:4300px" width="1200" height="64" viewBox="0 0 1200 64" aria-hidden="true">
    <path d="M0 64 C260 22 460 18 600 18 C740 18 940 22 1200 64 Z" fill="#27306e"/>
    <path d="M0 64 C260 22 460 14 600 14 C740 14 940 22 1200 64" fill="none" stroke="#0d9ad9" stroke-width="4"/>
  </svg>
  <div class="emblem" style="left:570px;top:4280px"></div>

  <div class="abs brand" style="left:0;width:1200px;justify-content:center;top:4406px;font-size:26px">
    <span class="dot" style="width:16px;height:16px"></span>BRIGHTWATER SYSTEMS
  </div>

  <div class="foot-col" style="left:157px">
    <h5>SERVICES</h5>
    <ul>
      <li>Dedicated Teams</li><li>Product Strategy</li><li>Product Engineering</li><li>Architecture</li><li>UX / UI Design</li><li>App Developers</li><li>QA &amp; Testing</li><li>Cyber Security</li><li>Web Development</li><li>Software Development</li>
    </ul>
  </div>
  <div class="foot-col" style="left:338px">
    <h5>TECHNOLOGIES</h5>
    <ul><li>Internet of Things</li><li>Blockchain</li><li>Cloud Computing</li></ul>
  </div>
  <div class="foot-col" style="left:521px">
    <h5>PLATFORMS</h5>
    <ul><li>Mobile Apps</li><li>Tablet Apps</li><li>Desktop Apps</li><li>Hybrid Platform</li><li>Cloud Hosting</li></ul>
  </div>
  <div class="foot-col" style="left:705px">
    <h5>COMPANY</h5>
    <ul><li>About</li><li>Services</li><li>Blogs</li><li>FAQ</li></ul>
  </div>
  <div class="foot-col" style="left:885px">
    <h5>CONTACT US</h5>
    <ul>
      <li class="ci"><svg width="10" height="10" viewBox="0 0 10 10" aria-hidden="true"><path d="M2 1 L4 1 L5 3 L4 4 C4.5 5.5 5 6 6 6.5 L7 5.5 L9 6.5 L9 8.5 C5 9 1 5 2 1 Z" fill="#0d9ad9"/></svg>555-014-2620</li>
      <li class="ci"><svg width="10" height="10" viewBox="0 0 10 10" aria-hidden="true"><path d="M2 1 L4 1 L5 3 L4 4 C4.5 5.5 5 6 6 6.5 L7 5.5 L9 6.5 L9 8.5 C5 9 1 5 2 1 Z" fill="#0d9ad9"/></svg>555-014-2620</li>
      <li class="ci"><svg width="10" height="8" viewBox="0 0 10 8" aria-hidden="true"><rect x="0.5" y="0.5" width="9" height="7" fill="#0d9ad9"/><path d="M0.5 0.5 L5 4 L9.5 0.5" fill="none" stroke="#27306e" stroke-width="1"/></svg>hello@brightwatersys.com</li>
      <li style="height:12px"></li>
      <li class="ci"><svg width="10" height="12" viewBox="0 0 10 12" aria-hidden="true"><path d="M5 11 C2 7 1 5.5 1 4.5 A4 4 0 0 1 9 4.5 C9 5.5 8 7 5 11 Z" fill="#0d9ad9"/><circle cx="5" cy="4.5" r="1.5" fill="#27306e"/></svg>1840 Harbor Lane NW</li>
      <li style="padding-left:18px">Suite 210, Lakeview</li>
      <li style="padding-left:18px">MI 49000</li>
    </ul>
  </div>

  <div class="abs copy">Copyright © 2021 Brightwater Systems. All rights reserved.</div>
</div>
</body>
</html>
```